Cannabis Dispensary Menu - Digital TV Display

This will be posted in a store on a tv to display all the products they have.
I have all the menu items added to a .psd file for you to work with already. I'm just looking for a good looking design thats also readable. The image size should be 1,920 x 1,080 pixels so that it displays well on a TV. I'd like categories/sub-categories to be separated from each other with some design elements. Another idea to save space would be to replace the CBD: and THC: labels with some kind of small icon that represents them

Target Market(s)

Cannabis consumers

Industry/Entity Type

Cannabis

Font styles to use
Sans Serif

Requirements
Must have
• The menu changes frequently so I will need a finished file I can edit.

```html
<!DOCTYPE html>
<html lang="en">
<head>
<meta charset="utf-8">
<title>Harbor Leaf Collective – Menu Board</title>
<link href="https://fonts.googleapis.com/css2?family=Arimo:ital,wght@0,400;0,700;1,700&display=swap" rel="stylesheet">
<style>
:root{
  --bg:#2f5b52;
  --bg-deep:#1d3e35;
  --pill:#0f2f27;
  --card:#ffffff;
  --ink:#1f2a2a;
  --navy:#173d6e;
  --red:#e01b22;
  --price:#a51f3c;
  --green:#5cae3a;
  --olive:#8d8a10;
  --leafgreen:#1f7a3a;
  --teal:#1a7c7c;
  --pink:#fbe6ea;
  --cream:#f5f8dc;
  --grey:#d3dcdb;
  --mist:#e4eaec;
}
*{margin:0;padding:0;box-sizing:border-box}
html,body{width:1200px;height:675px;overflow:hidden}
body{font-family:"Arimo",Arial,sans-serif;color:var(--ink);font-size:12.5px}
.board{position:relative;width:1200px;height:675px;background:linear-gradient(var(--bg) 0 640px,var(--bg-deep) 640px);overflow:hidden}
.abs{position:absolute}
.card{position:absolute;background:var(--card);border-radius:26px;overflow:hidden}
.pill{position:absolute;background:var(--pill);color:#fff;border-radius:16px;display:flex;align-items:center;justify-content:center;font-size:19px}
.head-pill{position:absolute;background:linear-gradient(#3d6f62,#1e473d);color:#fff;border-radius:20px;display:flex;align-items:center;justify-content:space-between;padding:0 24px;font-weight:700;font-size:31px;letter-spacing:.5px}
.leaf-mark{width:16px;height:16px;border-radius:50%;background:#fff}
.list{position:absolute;list-style:none}
.list li{display:flex;justify-content:space-between;height:15.6px;line-height:15.6px;white-space:nowrap}
.band{position:absolute}
.navy{color:var(--navy)}
.price{color:var(--price)}
.red-it{color:var(--red);font-weight:700;font-style:italic}
.title{font-weight:700;color:var(--navy)}
.bold{font-weight:700}
.photo{position:absolute;border-radius:40%}
.rule{position:absolute;height:1px;background:#9aa5a5}
.center{text-align:center}
</style>
</head>
<body>
<div class="board">

  <!-- ===== FLOWER ===== -->
  <section class="card" style="left:30px;top:28px;width:368px;height:633px">
    <div class="band" style="left:0;top:202px;width:368px;height:107px;background:var(--pink)"></div>
    <div class="band" style="left:0;top:309px;width:368px;height:131px;background:var(--cream)"></div>
    <div class="band" style="left:0;top:571px;width:368px;height:62px;background:var(--grey)"></div>
  </section>
  <div class="head-pill" style="left:56px;top:12px;width:322px;height:39px">
    <span class="leaf-mark" role="img" aria-label="cannabis leaf icon"></span>FLOWER<span class="leaf-mark" role="img" aria-label="cannabis leaf icon"></span>
  </div>

  <div class="abs" style="left:50px;top:58px;font-size:26px;line-height:30px"><span class="red-it">$50</span> <span class="navy">oz’s</span></div>
  <div class="pill" style="left:155px;top:56px;width:231px;height:30px">Indica</div>
  <ul class="list" style="left:52px;top:93px;width:150px">
    <li><span>Blueberry</span><span>28%</span></li>
    <li><span>Purple Vapor</span><span>27%</span></li>
    <li><span>Purple Kush</span><span>26%</span></li>
    <li><span>Ice Cream Cake</span><span>25%</span></li>
    <li><span>Garlic Breath</span><span>24%</span></li>
    <li><span>Master Kush</span><span>24%</span></li>
    <li><span>Kushy Kush</span><span>24%</span></li>
    <li><span>G13 Haze</span><span>24%</span></li>
  </ul>
  <ul class="list" style="left:217px;top:93px;width:168px">
    <li><span>Island Pink Kush</span><span>24%</span></li>
    <li><span>Green Crack</span><span>24%</span></li>
    <li><span>White Rhino</span><span>24%</span></li>
    <li><span>Pink Kush</span><span>21%</span></li>
    <li><span>Grape Ape</span><span>21%</span></li>
    <li><span>Peyote Cookies</span><span>22%</span></li>
    <li><span>God Bud</span><span>20%</span></li>
  </ul>

  <div class="pill" style="left:158px;top:221px;width:230px;height:28px">Hybrid</div>
  <ul class="list" style="left:51px;top:255px;width:152px">
    <li><span>Girl Scout Cookies</span><span>28%</span></li>
    <li><span>Peanutbutter Breath</span><span>28%</span></li>
    <li><span>Tangie</span><span>28%</span></li>
    <li><span>White Widow</span><span>26%</span></li>
  </ul>
  <ul class="list" style="left:220px;top:255px;width:160px">
    <li><span>Gelato</span><span>25%</span></li>
    <li><span>Miracle Alien Cookies</span><span>22%</span></li>
    <li><span>Chem Dog</span><span>19%</span></li>
    <li><span>Grape God</span><span>20%</span></li>
  </ul>

  <div class="pill" style="left:160px;top:326px;width:231px;height:28px">Sativa</div>
  <ul class="list" style="left:53px;top:362px;width:149px">
    <li><span>King Tut</span><span>33%</span></li>
    <li><span>Gamma Banner</span><span>29%</span></li>
    <li><span>Pineapple Express</span><span>25%</span></li>
  </ul>
  <div class="photo" role="img" aria-label="Photo of a dried cannabis flower bud" style="left:236px;top:355px;width:142px;height:64px;background:radial-gradient(#8a8a6a,#5b5a3e 70%,transparent 72%)"></div>
  <div class="abs" style="left:52px;top:427px;display:flex;align-items:center;gap:12px">
    <span class="bold" style="color:var(--teal);font-size:18px">CBD</span>
    <span style="color:#333">Candida - CBD: 20%, THC: 0.01%</span>
  </div>

  <div class="pill" style="left:160px;top:454px;width:231px;height:29px">AAAA+</div>
  <div class="abs bold" style="left:54px;top:490px;font-size:19px;color:var(--leafgreen)">Indica</div>
  <div class="abs bold" style="left:242px;top:491px;font-size:19px;color:var(--olive)">Hybrid</div>
  <ul class="list" style="left:54px;top:516px;width:170px">
    <li><span>Royal Pink Kush</span><span>28%</span></li>
    <li><span>3.5g</span><span class="price">$25</span></li>
    <li><span>7g</span><span class="price">$45</span></li>
    <li><span>14g</span><span class="price">$85</span></li>
    <li><span>28g</span><span class="price">$160</span></li>
  </ul>
  <ul class="list" style="left:243px;top:516px;width:131px">
    <li><span>Kingdom Kush</span><span>30%</span></li>
    <li><span>3.5g</span><span class="price">$30</span></li>
    <li><span>7g</span><span class="price">$50</span></li>
    <li><span>14g</span><span class="price">$90</span></li>
    <li><span>28g</span><span class="price">$160</span></li>
  </ul>

  <div class="abs title" style="left:54px;top:609px;font-size:17px">Pre-Rolls</div>
  <div class="abs red-it" style="left:52px;top:629px;font-size:17px">1-$5 or 2-$8</div>
  <ul class="list" style="left:194px;top:606px;width:90px;color:#333">
    <li>GMO</li><li>Kushy Kush</li><li>Master Kush</li>
  </ul>
  <ul class="list" style="left:294px;top:606px;width:90px;color:#333">
    <li>Grape Ape</li><li>Green Crack</li><li>White Widow</li>
  </ul>

  <!-- ===== CONCENTRATES ===== -->
  <section class="abs" style="left:419px;top:61px;width:365px;height:602px;border-radius:26px;background:linear-gradient(#b8c9c3,#6f928a 20%,#6f928a)"></section>
  <div class="abs" style="left:414px;top:462px;width:20px;height:82px;background:#3f5f57"></div>
  <div class="abs bold" style="left:567px;top:77px;font-size:31px;color:#fff">Concentrates</div>
  <div class="abs" style="left:433px;top:121px;width:339px;height:423px;background:#fff"></div>

  <div class="abs" style="left:405px;top:14px;width:190px;height:86px;border-radius:50%;background:var(--mist);transform:rotate(-12deg)"></div>
  <div class="abs bold center" style="left:430px;top:40px;width:140px;font-size:16px;line-height:18px;color:var(--navy)">Harbor Leaf<br>Collective</div>

  <div class="band" style="left:438px;top:125px;width:328px;height:32px;background:var(--pink)"></div>
  <div class="abs title" style="left:450px;top:128px;font-size:22px">Live Resin</div>
  <div class="abs red-it" style="left:576px;top:131px;font-size:19px">1g - $30 or 5g - $100</div>
  <ul class="list" style="left:451px;top:165px;width:160px">
    <li><span>Blackberry</span><span style="color:var(--green)">(Indica)</span></li>
    <li><span>Blue Dream</span><span style="color:var(--green)">(Hybrid)</span></li>
    <li><span>Gummy Bear</span><span style="color:var(--green)">(Hybrid)</span></li>
    <li><span>Gamma Banner</span><span style="color:var(--green)">(Hybrid)</span></li>
    <li><span>Sunrise Star</span><span style="color:var(--green)">(Sativa)</span></li>
  </ul>
  <div class="photo" role="img" aria-label="Photo of golden live resin concentrate" style="left:636px;top:160px;width:117px;height:86px;background:radial-gradient(#f4eab0,#d9c873 70%,transparent 72%)"></div>

  <div class="band" style="left:438px;top:252px;width:328px;height:32px;background:var(--pink)"></div>
  <div class="abs title" style="left:452px;top:256px;font-size:22px">Shatter</div>
  <div class="abs red-it" style="left:577px;top:259px;font-size:19px">1g - $30 or 5g - $100</div>
  <ul class="list" style="left:452px;top:291px;width:159px">
    <li><span>Bubba Kush</span><span>(Indica)</span></li>
    <li><span>Death Star</span><span>(Indica)</span></li>
    <li><span>M.A.C. 1</span><span>(Hybrid)</span></li>
    <li><span>Biscotti</span><span>(Hybrid)</span></li>
    <li><span>Amnesia Haze</span><span>(Sativa)</span></li>
  </ul>
  <div class="photo" role="img" aria-label="Photo of amber cannabis shatter" style="left:624px;top:288px;width:129px;height:88px;background:radial-gradient(#f6b21e,#c9730a 70%,transparent 72%)"></div>

  <div class="abs" style="left:437px;top:381px;width:135px;height:78px;background:var(--cream)"></div>
  <div class="abs title center" style="left:437px;top:386px;width:135px;font-size:22px">Diamonds</div>
  <div class="abs center" style="left:437px;top:414px;width:135px">THCA Diamonds</div>
  <div class="abs bold center" style="left:437px;top:431px;width:135px;font-size:14px">3.5g - <span class="price">$50</span></div>

  <div class="abs" style="left:584px;top:381px;width:183px;height:78px;background:var(--cream)"></div>
  <div class="abs title" style="left:584px;top:385px;width:170px;text-align:right;font-size:22px">Oil</div>
  <div class="abs" style="left:596px;top:410px;line-height:15.6px">Heritage Oil<br>Full Extract Cannabis Oil</div>
  <div class="abs bold price" style="left:593px;top:440px;font-size:12.5px">1g - $30 | 3g - $100 | 5g $200</div>

  <div class="abs" style="left:434px;top:462px;width:338px;height:82px;background:var(--pink)"></div>
  <div class="abs title" style="left:452px;top:496px;font-size:22px">Hash</div>
  <div class="abs center" style="left:511px;top:476px;width:100px;font-size:14px;line-height:18px"><b>Black Magic</b><br>1g - <span class="price">$15</span><br>5g - <span class="price">$50</span></div>
  <div class="abs center" style="left:612px;top:476px;width:80px;font-size:14px;line-height:18px"><b>XXX</b><br>1g - <span class="price">$15</span><br>5g - <span class="price">$50</span></div>
  <div class="abs center" style="left:684px;top:476px;width:80px;font-size:14px;line-height:18px"><b>XX</b><br>1g - <span class="price">$7</span><br>5g - <span class="price">$25</span></div>

  <div class="abs" style="left:419px;top:544px;width:365px;height:119px;border-radius:0 0 26px 26px;background:linear-gradient(#fbfcee,#f1f4cf)"></div>
  <div class="abs title center" style="left:419px;top:550px;width:350px;font-size:30px">Vapes</div>
  <div class="abs" style="left:453px;top:591px;line-height:15.6px">Skyline&nbsp; 1g<br>Distillate&nbsp;&nbsp; <span class="price">$35</span><br>Premium&nbsp;&nbsp; <span class="price">$39</span></div>
  <div class="abs center" style="left:554px;top:592px;width:100px;line-height:15.6px">Night Cap 1g<br>1 - <span class="price">$30</span><br>3 - <span class="price">$75</span></div>
  <div class="abs center" style="left:674px;top:592px;width:100px;line-height:15.6px">Lightning 1g<br>1 - <span class="price">$30</span><br>3 - <span class="price">$75</span></div>

  <!-- ===== EDIBLES ===== -->
  <section class="card" style="left:803px;top:18px;width:367px;height:641px"></section>
  <div class="head-pill" style="left:827px;top:19px;width:321px;height:38px">
    <span class="leaf-mark" role="img" aria-label="cannabis leaf icon"></span>EDIBLES<span class="leaf-mark" role="img" aria-label="cannabis leaf icon"></span>
  </div>

  <ul class="list" style="left:824px;top:74px;width:192px">
    <li><span>Shatter Chews 150mg</span><span class="price">$20</span></li>
    <li><span>Shatter Bar 500mg</span><span class="price">$30</span></li>
    <li><span>Fuel Crew Gummies 500mg</span><span class="price">$25</span></li>
  </ul>
  <div class="rule" style="left:824px;top:125px;width:198px"></div>
  <div class="abs" style="left:824px;top:129px;line-height:15.6px;width:192px"><b>Trailhead Gummies</b><br>500mg - <span class="price">$30</span> &nbsp;| &nbsp;3000mg<span class="price" style="float:right">$50</span></div>
  <div class="rule" style="left:824px;top:164px;width:198px"></div>
  <div class="abs" style="left:824px;top:168px;line-height:15.6px;width:205px">West Shore Gummies 600mg&nbsp; <span class="price">$30</span><br>Fizz Pop 60mg <span class="price">1 - $15 or 3 - $40</span></div>
  <div class="rule" style="left:824px;top:204px;width:198px"></div>
  <div class="abs" style="left:824px;top:206px;line-height:15.6px"><b>Canna Caps</b><br>CBD: 13mg, THC: 145mg - <span class="price">$20</span></div>
  <div class="rule" style="left:824px;top:244px;width:198px"></div>
  <div class="abs" style="left:824px;top:253px;line-height:15.6px"><b>Canna Sugar</b><br>CBD: 15mg, THC: 50mg - <span class="price">$5</span></div>

  <div class="abs" style="left:1052px;top:73px;line-height:15.6px"><b>Canna Cookies</b>
    <div style="padding-left:17px">50mg - <span class="price">$5</span><br>100mg - <span class="price">$10</span><br>156mg - <span class="price">$15</span></div></div>
  <div class="abs" style="left:1052px;top:143px;line-height:15.6px"><b>HLC Chocolates</b>
    <div style="padding-left:17px">100mg - <span class="price">$10</span><br>150mg - <span class="price">$15</span><br>250mg - <span class="price">$25</span></div></div>
  <div class="abs" style="left:1052px;top:214px;line-height:15.6px"><b>HLC Gummies</b>
    <div style="padding-left:17px">20mg - <span class="price">$2</span><br>100mg - <span class="price">$10</span><br>200mg - <span class="price">$20</span><br>300mg - <span class="price">$30</span></div></div>

  <div class="abs" style="left:808px;top:300px;width:358px;height:189px;background:var(--pink)"></div>
  <div class="abs title" style="left:823px;top:305px;font-size:22px">Holistic Health Essentials</div>
  <ul class="list" style="left:822px;top:337px;width:178px">
    <li><b>CBD Oil</b></li>
    <li><span>CBD: 1000mg</span><span class="price">$40</span></li>
    <li><span>CBD: 5000mg</span><span class="price">$200</span></li>
    <li><b>CBD VG Tincture</b></li>
    <li><span>CBD: 200mg THC: 60mg</span><span class="price">$40</span></li>
    <li><b>THC VG Tincture</b></li>
    <li><span>CBD: 13mg THC: 450mg</span><span class="price">$40</span></li>
    <li><span>CBD Patch CBD: 20mg</span><span class="price">$20</span></li>
    <li><span>CBD Cream CBD: 3000mg</span><span class="price">$20</span></li>
  </ul>
  <ul class="list" style="left:1014px;top:338px;width:150px">
    <li><b>Topical Cream</b></li>
    <li>THC: 500mg CBD: 50mg</li>
    <li><span>Small</span><span class="price" style="width:40px">$10</span></li>
    <li><span>Large</span><span class="price" style="width:40px">$25</span></li>
  </ul>
  <ul class="list" style="left:1014px;top:416px;width:152px">
    <li><b>Bath Bombs CBD: 10mg</b></li>
    <li><span>THC: 50mg</span><span class="price" style="width:52px">$5</span></li>
    <li><span>THC: 100mg</span><span class="price" style="width:52px">$10</span></li>
    <li><span>THC: 150mg</span><span class="price" style="width:52px">$15</span></li>
  </ul>

  <div class="abs title" style="left:823px;top:496px;font-size:25px;line-height:28px">Pet<br>Care</div>
  <div class="abs" role="img" aria-label="Silhouette of a dog and cat" style="left:888px;top:512px;width:42px;height:45px;border-radius:40% 40% 8px 8px;background:#111"></div>
  <div class="abs" style="left:944px;top:497px;line-height:15.6px"><b>CBD Cat Treats</b><br>THC: 0.5mg<br>CBD: 5mg<br><span class="price">$10</span></div>
  <svg class="abs" style="left:1014px;top:502px" width="38" height="58" viewBox="0 0 38 58"><line x1="36" y1="1" x2="2" y2="57" stroke="#173d6e" stroke-width="2"/></svg>
  <div class="abs" style="left:1053px;top:498px;line-height:15.6px"><b>CBD Dog Treats</b><br>THC:2mg<br>CBD: 5.6mg<br><span class="price">$10</span></div>

  <div class="abs" style="left:819px;top:583px;width:337px;height:67px;border-radius:24px;background:var(--mist)"></div>
  <div class="abs title center" style="left:819px;top:568px;width:340px;font-size:28px">Seasonal</div>
  <div class="abs center" style="left:819px;top:603px;width:340px;font-size:15px;line-height:19px">Christmas THC Crackers - <span class="price">$15</span><br>Christmas&nbsp; Edible Advent Calendars - <span class="price">$80</span></div>

</div>
</body>
</html>
```